1 Page Bio, describing our Mission to buy multifamily properties in Colorado Springs.

I am uploading a sample of an associate who is doing a similar thing in Tampa Florida. I will also upload an attempt by my assistant to make the flyer and I will upload 3 pictures to use, along with another document that has text to add. I want to be able to edit the document pretty easily inside a google doc. thanks, I want it to look clean and professional.

```html
<!DOCTYPE html>
<html lang="en">
<head>
<meta charset="utf-8">
<title>Norwick Multifamily – One Page Bio</title>
<link href="https://fonts.googleapis.com/css2?family=Oswald:wght@500;600&family=Montserrat:wght@400;500;600;700&display=swap" rel="stylesheet">
<style>
  :root{
    --teal:#0f6f69;
    --teal-dark:#0b5650;
    --ink:#2b2b2b;
    --grey-bg:#f1f2f3;
    --right-bg:#e4e7ea;
    --footer-dark:#3b4556;
    --footer-blue:#5d7598;
    --white:#ffffff;
  }
  *{box-sizing:border-box;margin:0;padding:0}
  html,body{width:850px;height:1200px;overflow:hidden;background:#fff}
  body{font-family:"Montserrat",Arial,sans-serif;color:var(--ink)}
  .flyer{position:relative;width:850px;height:1200px;overflow:hidden;background:var(--grey-bg)}
  .abs{position:absolute}
  .right-panel{left:494px;top:0;width:356px;height:1152px;background:linear-gradient(180deg,var(--right-bg) 0%,#f4f5f6 45%,#fafafa 100%)}
  .hero{left:0;top:0}
  .brand{left:134px;top:0;width:218px;height:148px;background:var(--teal);display:flex;flex-direction:column;align-items:center;justify-content:center;gap:10px}
  .brand-mark{width:22px;height:22px;border:2px solid var(--white)}
  .brand-name{font-weight:600;color:var(--white);font-size:19px;letter-spacing:1px}

  .condensed{white-space:nowrap;transform:scaleX(.78);transform-origin:left top}
  .headline{left:34px;top:168px;font-family:"Oswald",sans-serif;font-weight:500;color:var(--white);font-size:38px;line-height:46px;text-shadow:0 2px 4px rgba(0,0,0,.35);transform:scaleX(.76)}
  .h-teal{font-family:"Oswald",sans-serif;font-weight:500;color:var(--teal-dark);text-transform:uppercase}

  .mission{left:554px;width:290px}
  .mission .icon{position:absolute;left:0;top:0}
  .mission h3{position:absolute;left:54px;top:8px;font-size:20px;line-height:22px;transform:scaleX(.74)}
  .mission p{position:absolute;left:56px;top:38px;font-size:12.3px;line-height:15.6px;color:#3a3a3a;white-space:nowrap}

  .principals-title{left:520px;top:484px;font-size:30px;line-height:36px;transform:scaleX(.76)}
  .person-name{font-size:17px;font-weight:500;color:#222;line-height:20px}
  .bullets{list-style:none;font-size:10.3px;line-height:13px;color:#333}
  .bullets li{position:relative;padding-left:10px}
  .bullets li::before{content:"";position:absolute;left:0;top:4.5px;width:5px;height:5px;border-radius:50%;background:#222}
  .principal-list{font-size:10.8px;line-height:13px}

  .market-title{right:394px;top:552px;font-size:32px;line-height:40px;text-align:right;transform:scaleX(.8);transform-origin:right top}
  .market-copy{right:394px;top:648px;width:400px;text-align:right;font-size:12.3px;line-height:15.5px;color:#333}

  .section-title{font-size:27px;line-height:30px}
  .list-lg{font-size:12.2px;line-height:15px}
  .list-lg li{padding-left:12px}
  .list-lg li::before{top:4.5px;width:6px;height:6px}

  .divider{height:1px;background:#777}
  .divider::before,.divider::after{content:"";position:absolute;top:-2.5px;width:6px;height:6px;border-radius:50%;background:#777}
  .divider::before{left:-3px}.divider::after{right:-3px}

  .advisor-photo{width:84px;height:84px;background:linear-gradient(180deg,#d9d9d9,#8c8c8c);border:1px solid #bbb}
  .advisor-list{font-size:9.3px;line-height:12px;color:#333}
  .advisor-list li{text-align:justify}
  .advisor-list li::before{top:4px;width:4px;height:4px}

  .strategy-col h4{font-family:"Oswald",sans-serif;font-weight:500;font-size:17px;line-height:20px;color:#2a2a2a;margin:0 0 10px 7px;white-space:nowrap;transform:scaleX(.82);transform-origin:left top}
  .strategy-col .bullets{font-size:9.6px;line-height:12px}
  .strategy-col .bullets li::before{top:4px;width:4px;height:4px;background:#444}
  .vrule{width:1px;background:#bbb}

  .footer{left:0;top:1152px;width:850px;height:48px;background:var(--footer-blue)}
  .footer-cta{position:absolute;left:0;top:0;width:192px;height:48px;background:var(--footer-dark);color:var(--white);font-weight:700;font-size:18px;display:flex;align-items:center;justify-content:center}
  .footer-contact{position:absolute;left:207px;top:6px;color:var(--white)}
  .footer-contact .fc-name{font-size:15px;font-weight:500;line-height:19px}
  .footer-contact .fc-mail{font-size:11.5px;line-height:14px;display:flex;align-items:center;gap:4px}
  .footer-phone{position:absolute;left:390px;top:8px;display:flex;align-items:center;gap:8px;color:var(--white);font-weight:700;font-size:25px;line-height:32px}
  .footer-web{position:absolute;left:645px;top:17px;color:var(--white);font-size:11px;letter-spacing:3.6px;white-space:nowrap}
</style>
</head>
<body>
<div class="flyer">

  <div class="abs right-panel"></div>

  <svg class="abs hero" width="850" height="700" viewBox="0 0 850 700">
    <defs>
      <linearGradient id="sky" x1="0" y1="0" x2="0" y2="1">
        <stop offset="0" stop-color="#1d2a44"/>
        <stop offset=".45" stop-color="#4d6280"/>
        <stop offset=".75" stop-color="#b7905f"/>
        <stop offset="1" stop-color="#6a4a3a"/>
      </linearGradient>
      <path id="captionArc" d="M480.6 408 A96 96 0 0 0 647.4 408"/>
    </defs>
    <path d="M0 640 C150 560 330 450 494 385 L494 440 C330 500 170 570 60 648 Z" fill="#cfd2d6"/>
    <path d="M0 0 H494 V295 C350 360 170 470 0 590 Z" fill="url(#sky)" role="img" aria-label="Photo of a modern multifamily residential tower at sunset"/>
    <path d="M0 590 C170 470 350 360 494 295 L494 385 C330 450 150 560 0 640 Z" fill="#ffffff"/>
    <path d="M850 282 L850 345 C800 385 740 420 706 432 C690 420 660 398 640 382 C710 392 780 345 850 282 Z" fill="var(--teal)"/>
    <circle cx="564" cy="360" r="76" fill="#ffffff"/>
    <circle cx="564" cy="360" r="70" fill="#5f7a5e" role="img" aria-label="Photo of the two principals outdoors"/>
    <text font-family="Montserrat, sans-serif" font-size="12" fill="#333"><textPath href="#captionArc" startOffset="50%" text-anchor="middle">Dale &amp; Glen Norwick</textPath></text>
  </svg>

  <div class="abs brand">
    <div class="brand-mark"></div>
    <div class="brand-name">RIDGELINE HOME</div>
  </div>

  <h1 class="abs headline condensed">ACQUIRING VALUE-ADD MULTIFAMILY<br>REAL ESTATE IN COLORADO SPRINGS</h1>

  <div class="abs mission" style="top:36px;height:90px">
    <svg class="icon" width="42" height="42" viewBox="0 0 42 42"><circle cx="21" cy="21" r="19" fill="none" stroke="var(--teal)" stroke-width="2"/><circle cx="21" cy="21" r="11" fill="none" stroke="var(--teal)" stroke-width="2"/><circle cx="21" cy="21" r="5" fill="none" stroke="var(--teal)" stroke-width="2"/><path d="M21 21 L31 11 M28 10 h4 v4" fill="none" stroke="var(--teal)" stroke-width="2"/></svg>
    <h3 class="h-teal condensed">Our Mission</h3>
    <p>To create a family business<br>by purchasing Multifamily<br>Residences, one at a time.</p>
  </div>
  <div class="abs mission" style="top:121px;height:90px">
    <svg class="icon" width="42" height="42" viewBox="0 0 42 42"><circle cx="21" cy="21" r="19" fill="none" stroke="var(--teal)" stroke-width="2"/><path d="M8 19 l7-4 6 3 6-3 7 4 -7 6 -6-2 -6 2 z" fill="var(--teal)"/></svg>
    <h3 class="h-teal condensed">Our Values</h3>
    <p>To provide a white glove experience<br>to allresidences with a clean,<br>safe, and fun environment.</p>
  </div>
  <div class="abs mission" style="top:207px;height:80px">
    <svg class="icon" width="42" height="42" viewBox="0 0 42 42"><circle cx="21" cy="21" r="19" fill="none" stroke="var(--teal)" stroke-width="2"/><circle cx="21" cy="21" r="9" fill="none" stroke="var(--teal)" stroke-width="4" stroke-dasharray="4 3"/><circle cx="21" cy="21" r="3" fill="var(--teal)"/></svg>
    <h3 class="h-teal condensed">The Process</h3>
    <p>Buy right, manage right,<br>and finance right.</p>
  </div>

  <h2 class="abs h-teal condensed principals-title">Principals:</h2>
  <div class="abs person-name" style="left:524px;top:528px">Dale Norwick</div>
  <ul class="abs bullets principal-list" style="left:516px;top:555px;width:332px">
    <li>Licensed Colorado Real Estate Agent 18 years.</li>
    <li>Broker-Owner of two HomeKey Franchises 7 and 2 Years.</li>
    <li>Real Estate investing for 5 years.</li>
    <li>Member of Keystone Investors Academy.</li>
    <li>Married 24 years to Joan, parenting 10 children together. Appeared on Sam and Leo's Multi-Family Hour podcast</li>
    <li>Episode 43<br>$2M portfolio.</li>
  </ul>
  <div class="abs person-name" style="left:522px;top:679px">Glen Norwick</div>
  <ul class="abs bullets principal-list" style="left:516px;top:705px;width:332px">
    <li>Retired Electrical Engineer.</li>
    <li>Active Real Estate Investor/Consultant.</li>
    <li>Net worth over $4M</li>
    <li>15 Grandchildren.</li>
  </ul>

  <svg class="abs" style="left:396px;top:480px" width="56" height="56" viewBox="0 0 56 56" fill="none" stroke="var(--teal)" stroke-width="2.4">
    <path d="M4 24 L28 4 L52 24"/><path d="M10 20 V50 H46 V20"/><path d="M17 44 V36 M24 44 V31 M31 44 V34 M38 44 V26"/><path d="M16 32 L24 25 L30 29 L40 19 M36 19 h4 v4"/><path d="M2 52 H54"/>
  </svg>
  <h2 class="abs h-teal market-title" style="white-space:nowrap">The Market:<br>Colorado Springs</h2>
  <p class="abs market-copy">Projected job growth of nearly 50%<br>Below average unemployment rates.<br>Above-average incomes.<br>Solid economy, military, aerospace, electronics industry,<br>and tourism.<br>The Target : B and C class assets located in Colorado Springs<br>or nearby submarkets.</p>

  <h2 class="abs h-teal condensed section-title" style="left:40px;top:797px">Why Multifamily?</h2>
  <ul class="abs bullets list-lg" style="left:27px;top:841px">
    <li>Earn monthly cashflow</li>
    <li>Huge TAX Benefits</li>
    <li>Passive Income</li>
    <li>Historically Stable Investments</li>
    <li>Economies of Scale</li>
    <li>Housing is an enduring need</li>
  </ul>
  <h2 class="abs h-teal condensed section-title" style="left:246px;top:797px">Why Colorado Springs?</h2>
  <ul class="abs bullets list-lg" style="left:241px;top:841px">
    <li>Strong Job Growth 2.91%</li>
    <li>Robust Population Growth 1.95%</li>
    <li>20.5% Population increase by 2030</li>
    <li>Low Unemployment Rate 2.9%</li>
    <li>Many large firms relocating to<br>Colorado Spring</li>
  </ul>

  <div class="abs divider" style="left:526px;top:808px;width:62px"></div>
  <h2 class="abs h-teal condensed section-title" style="left:638px;top:792px">Advisors</h2>
  <div class="abs divider" style="left:756px;top:808px;width:62px"></div>

  <div class="abs advisor-photo" style="left:508px;top:846px" role="img" aria-label="Portrait photo of advisor Grant Ellison"></div>
  <div class="abs" style="left:604px;top:844px;width:240px">
    <div class="person-name">Grant Ellison</div>
    <ul class="bullets advisor-list" style="margin-top:3px">
      <li>General partner on 103 Apartments</li>
      <li>Acquiring 101 more apartments in Q1 - 2020</li>
      <li>Flips 4-8 houses a year</li>
      <li>Active member in the Sam &amp; Leo Community</li>
      <li>Accountability coach</li>
    </ul>
  </div>

  <div class="abs advisor-photo" style="left:508px;top:982px" role="img" aria-label="Portrait photo of advisor Neil Barrow"></div>
  <div class="abs" style="left:604px;top:956px;width:230px">
    <div class="person-name">Neil Barrow</div>
    <ul class="bullets advisor-list" style="margin-top:6px">
      <li>Neil is the owner/operator of Summit Residential Group and Summit Residential Management</li>
      <li style="margin-top:12px">He has been in the real estate business for 13 years and has created a portfolio of over 1000 units while growing Summit Management with team of 15 staff members.</li>
      <li style="margin-top:12px">He has taught real estate for the past 6 years and has dozens of highly successful students. Neil uses his extensive real estate experience to teach his students the "real" side of real estate.</li>
    </ul>
  </div>

  <div class="abs divider" style="left:28px;top:988px;width:96px"></div>
  <h2 class="abs h-teal condensed section-title" style="left:139px;top:972px">Investment Strategy</h2>
  <div class="abs divider" style="left:362px;top:988px;width:94px"></div>

  <div class="abs strategy-col" style="left:27px;top:1015px">
    <h4>ACQUIRE</h4>
    <ul class="bullets">
      <li>Purchase Underperforming</li>
      <li>Apartment Communities</li>
      <li>Mom and Pop Characteristies</li>
      <li>Class B and C Buildings</li>
      <li>20-50 units</li>
      <li>Deferred maintenance<br>Value-Add opportunity</li>
    </ul>
  </div>
  <div class="abs vrule" style="left:192px;top:1024px;height:104px"></div>
  <div class="abs strategy-col" style="left:203px;top:1015px">
    <h4>REPOSITION:</h4>
    <ul class="bullets">
      <li>Hire professional<br>management team</li>
      <li>Stabilize the property</li>
      <li>Fill vacancies</li>
      <li>implement RUBS</li>
      <li>Change fee structure</li>
      <li>Raise remaining rents</li>
    </ul>
  </div>
  <div class="abs vrule" style="left:332px;top:1024px;height:104px"></div>
  <div class="abs strategy-col" style="left:342px;top:1015px">
    <h4>REFINANCE &amp; PROCEEDS:</h4>
    <ul class="bullets">
      <li>Refinance the property<br>and roll proceeds into<br>the next</li>
      <li style="margin-top:12px">Sell the property and<br>cash out or roll into the<br>next property</li>
    </ul>
  </div>

  <div class="abs footer">
    <div class="footer-cta">Partner with us</div>
    <div class="footer-contact">
      <div class="fc-name">Dale &amp; Glen Norwick</div>
      <div class="fc-mail"><svg width="11" height="8" viewBox="0 0 11 8"><rect width="11" height="8" fill="#fff"/><path d="M0 0 L5.5 4.5 L11 0" fill="none" stroke="var(--footer-blue)" stroke-width="1"/></svg>dnorwick@mailbox.com</div>
    </div>
    <div class="footer-phone">
      <svg width="24" height="24" viewBox="0 0 24 24"><circle cx="12" cy="12" r="11" fill="none" stroke="#fff" stroke-width="2"/><path d="M8 6 l2 0 1 3 -1.5 1.2 c.8 1.8 2 3 3.8 3.8 L14.5 12.5 l3 1 0 2 c-5 .5 -10-4.5-9.5-9.5z" fill="#fff"/></svg>
      719-555-0148
    </div>
    <div class="footer-web">www.norwick.com</div>
  </div>

</div>
</body>
</html>
```